Boutique Wealth management firm needs a new business card design

I want to update my business card design to be more consistent with the look and feel of my website (www.corvalen-capital.example). I would like to incorporate an ivory parchment background and am open to switching from the current "portrait" layout to a more traditional "landscape" orientation. The final design should convey stability and exclusivity and I want something in PDF format that is ready to send to the printer
Updates

Thank you all for taking the time to submit your designs for my project. I've made my decision and picked the design I like best. Thanks again!

Industry/Entity Type

Business

```html
<!DOCTYPE html>
<html lang="en">
<head>
<meta charset="utf-8">
<title>Corvalen Capital – Business Card</title>
<link href="https://fonts.googleapis.com/css2?family=Montserrat:wght@600;700;800&family=Lato:wght@400;700&display=swap" rel="stylesheet">
<style>
  :root {
    --backdrop: #2a2a2b;
    --parchment-light: #e2c9a0;
    --parchment-mid: #d4b687;
    --parchment-dark: #b8966a;
    --rose: #a23e4e;
    --olive: #74742c;
    --tan: #b49a66;
    --plum: #7b2d63;
    --ink: #2b2620;
  }
  * { box-sizing: border-box; margin: 0; padding: 0; }
  html, body {
    width: 1200px; height: 997px; overflow: hidden;
    background: var(--backdrop);
  }
  .canvas { position: relative; width: 1200px; height: 997px; }

  .card {
    position: absolute;
    width: 560px; height: 320px;
    border-radius: 2px;
    background:
      radial-gradient(ellipse at 30% 35%, var(--parchment-light) 0%, var(--parchment-mid) 55%, var(--parchment-dark) 100%);
    overflow: hidden;
  }
  .card--front { left: 90px; top: 90px; }
  .card--back  { left: 550px; top: 560px; }

  /* Front */
  .headline {
    position: absolute; left: 38px; top: 48px;
    font-family: "Montserrat", sans-serif; font-weight: 800;
    font-size: 50px; line-height: 0.98; letter-spacing: 1px;
    color: var(--rose);
  }
  .headline .money { color: var(--olive); }
  .headline .mark {
    position: absolute; left: 322px; top: 62px;
    font-size: 150px; line-height: 1; color: var(--tan);
  }
  .brand {
    position: absolute;
    font-family: "Montserrat", sans-serif; font-weight: 700;
    color: var(--plum); letter-spacing: 0.5px; white-space: nowrap;
  }
  .card--front .brand { right: 34px; top: 182px; font-size: 22px; }

  /* Back */
  .card--back .brand { right: 30px; top: 34px; font-size: 24px; }
  .divider {
    position: absolute; left: 190px; right: 38px; top: 186px;
    height: 2px; background: var(--plum);
  }
  .person {
    position: absolute; left: 36px; top: 160px;
    font-family: "Montserrat", sans-serif;
  }
  .person .name { font-size: 19px; font-weight: 700; color: var(--plum); }
  .person .cred { font-size: 15px; color: var(--ink); margin-left: 10px; font-weight: 700; }
  .person .role { font-size: 17px; font-weight: 700; color: var(--ink); margin-top: 2px; }
  .contacts {
    position: absolute; left: 36px; top: 226px; list-style: none;
    font-family: "Lato", sans-serif; font-size: 15px; color: var(--ink);
  }
  .contacts li { display: flex; align-items: center; height: 26px; }
  .contacts svg { width: 16px; height: 16px; margin-right: 12px; flex: none; }
  .address {
    position: absolute; right: 38px; top: 200px; text-align: right;
    font-family: "Montserrat", sans-serif; font-weight: 600;
    font-size: 14px; line-height: 1.3; color: var(--ink);
  }
</style>
</head>
<body>
<main class="canvas">
  <section class="card card--front" aria-label="Business card front">
    <h1 class="headline">TIRED OF<br>WORRYING<br>ABOUT<br><span class="money">MONEY</span><span class="mark">?</span></h1>
    <div class="brand">CORVALEN CAPITAL</div>
  </section>

  <section class="card card--back" aria-label="Business card back">
    <div class="brand">CORVALEN CAPITAL</div>
    <div class="divider"></div>
    <div class="person">
      <div><span class="name">DANA WHITLOCK</span><span class="cred">CFP®</span></div>
      <div class="role">PRINCIPAL</div>
    </div>
    <ul class="contacts">
      <li>
        <svg viewBox="0 0 16 16" aria-hidden="true"><rect x="3.5" y="1" width="9" height="14" rx="1.5" fill="none" stroke="#7b2d63" stroke-width="1.4"/><line x1="7" y1="12.5" x2="9" y2="12.5" stroke="#7b2d63" stroke-width="1.2"/></svg>
        555-014-2087
      </li>
      <li>
        <svg viewBox="0 0 16 16" aria-hidden="true"><rect x="1" y="3" width="14" height="10" fill="#7b2d63"/><polyline points="1,3 8,9 15,3" fill="none" stroke="#d4b687" stroke-width="1.2"/></svg>
        dana@corvalen-capital.example
      </li>
      <li>
        <svg viewBox="0 0 16 16" aria-hidden="true"><g fill="none" stroke="#7b2d63" stroke-width="1.6" stroke-linecap="round"><path d="M7 9.5 L4.5 12 a2.2 2.2 0 0 1 -3 -3 L4 6.5 a2.2 2.2 0 0 1 3 0"/><path d="M9 6.5 L11.5 4 a2.2 2.2 0 0 1 3 3 L12 9.5 a2.2 2.2 0 0 1 -3 0"/><line x1="6" y1="10" x2="10" y2="6"/></g></svg>
        www.corvalen-capital.example
      </li>
    </ul>
    <address class="address">2280 Harbor Ridge Ave. #412<br>Alder Grove, CA 90000</address>
  </section>
</main>
</body>
</html>
```